Larkwell cyber security firm Website

We did our website ourselves on Joomla, it's not great. We want a wordpress based redesign. Some thing that will represent a modern cyber security firm that's aimed at solving business problems.
Https://larkwell.co.nz (current site)
#58427c - primary color (you'll know why when you see it's name)
Logo files can be provided. Ask for more info if you need.

We want a modern, quick to load website. Website is going to have a home - services - products - about us - blogs menu. Will need a footer menu, site map, contact page etc.
We getting Content done sperately.
Our logo is #58427c - so hoping for a light theme (or at least the top is).
While we have been specific around the color - we are not after a website that has too much of it.

Reference sites that we like :
https://www.tidemoor.co.nz/ - Love the full screen real world image
https://venlorix.co.nz/ (love the real world imagry and motion)
https://www.qavrel.com/us-en?lnk=m
https://ostwynde.com

Please dont use :
cartoon or redered images : (Like this : https://img.plumdexa.com/free-vector/cyber-security-concept_23-2148543851.jpg?w=2000 )

Please don't use images like this : https://www.merivast.com/eu/blog/oil-gas/app/uploads/2020/04/116137226_s-1440x564_c.jpg - they are old and boring.

We would like to see some creativity - loading our logo into a readymade wordpress template and hitting go won't cut it.

Thanks everyone who has submitted so far. We've extended the deadline as we wanted to give everyone a chance to Re- read the brief and perhaps make some tweeks should they feel it necessary.

Target Market(s)

Mid - large enterprise, finance, insurance, utilities vertical

Industry/Entity Type

Cyber security

Coding

Coded - Design and coding required

Number of Pages Required

5+ page

Font styles to use
Other font styles liked:
• Open sans

Colors

Designer to choose colors to be used in the design.

Requirements
Must have
• Simple clear messaging, something that catches user engagement
Nice to have
• Motion of some sort, but not overdone, GDPR

```html
<!DOCTYPE html>
<html lang="en">
<head>
<meta charset="utf-8">
<title>Larkwell — Cyber Security</title>
<link href="https://fonts.googleapis.com/css2?family=Open+Sans:wght@300;400;600;700&display=swap" rel="stylesheet">
<style>
:root{
  --primary:#58427c;
  --primary-soft:#7a64a0;
  --ink:#2b2b3a;
  --text:#5d5d6c;
  --muted:#9a9aa8;
  --line:#e4e4ea;
  --grey:#f3f3f6;
  --white:#ffffff;
  --stage:#eeeef1;
}
*{box-sizing:border-box;margin:0;padding:0}
html,body{width:1200px;height:2804px;overflow:hidden}
body{background:var(--stage);font-family:"Open Sans",Arial,sans-serif;color:var(--text);position:relative}
.site{position:absolute;left:160px;top:45px;width:880px;height:2714px;background:var(--white);overflow:hidden;box-shadow:0 6px 30px rgba(40,30,70,.08)}
.abs{position:absolute}
p{font-size:9px;line-height:1.7}

/* header */
.topbar{left:0;top:0;width:880px;height:40px;background:var(--white);border-bottom:1px solid var(--line);display:flex;align-items:center;justify-content:space-between;padding:0 44px;font-size:9px;color:var(--muted)}
.topbar span{display:flex;align-items:center;gap:6px}
.brand{left:0;top:0;width:880px;height:40px;display:flex;align-items:center;justify-content:center;gap:8px;font-size:17px;font-weight:700;color:var(--primary);letter-spacing:.5px}
.brand i{width:14px;height:14px;border-radius:50%;background:var(--primary);display:block}
.nav{left:44px;top:52px;width:792px;height:30px;display:flex;background:rgba(255,255,255,.92)}
.nav a{flex:1;font-size:8.5px;color:var(--ink);text-decoration:none;display:flex;align-items:center;justify-content:center;border-right:1px solid var(--line)}
.nav a:last-child{border-right:0}

/* hero */
.hero{left:0;top:40px;width:880px;height:448px;background:linear-gradient(120deg,#3b3f52 0%,#24283a 45%,#1a1d2b 100%)}
.hero-copy{right:60px;top:250px;width:420px;text-align:right;color:var(--white)}
.hero-copy .eyebrow{font-size:8px;letter-spacing:3px;text-transform:uppercase;color:#cfc4e6}
.hero-copy h1{font-size:36px;font-weight:400;line-height:1.15;margin-top:6px}
.btns{display:flex;gap:14px;justify-content:flex-end;margin-top:22px}
.btn{font-size:8px;font-weight:600;letter-spacing:1px;text-transform:uppercase;padding:9px 20px;color:var(--white)}
.btn.solid{background:var(--primary)}
.btn.line{border:1px solid var(--white)}

/* headings */
h2{font-size:24px;font-weight:400;color:var(--ink);line-height:1.2}
h2 b{font-weight:600;color:var(--primary)}
h2 em{font-style:normal;color:var(--primary)}
.more{font-size:8px;color:var(--ink);margin-top:18px;display:flex;align-items:center;gap:6px}

/* solutions */
.solutions-title{left:124px;top:595px}
.solutions-text{left:466px;top:590px;width:340px}

/* about */
.about-band{left:437px;top:780px;width:443px;height:395px;background:var(--grey)}
.about-img{left:124px;top:760px;width:313px;height:335px;background:linear-gradient(135deg,#c9ccd6,#8f94a3)}
.about-copy{left:480px;top:840px;width:330px}
.about-copy p{margin-top:18px}

/* services */
.services-title{left:124px;top:1222px}
.grid{left:124px;top:1285px;width:680px;height:410px;display:grid;grid-template-columns:repeat(4,1fr);grid-template-rows:1fr 1fr;gap:10px}
.shot{background:linear-gradient(180deg,#f6f6f8,#e3e3ea)}
.card{background:var(--white);padding:22px 16px}
.card h3{font-size:10px;font-weight:600;color:var(--ink)}
.card p{font-size:7.5px;margin-top:8px;line-height:1.6}
.card .more{margin-top:12px;font-size:7.5px}

/* what we do */
.work-band{left:0;top:1780px;width:700px;height:310px;background:var(--grey)}
.work-img{left:490px;top:1725px;width:313px;height:368px;background:linear-gradient(135deg,#4a4e5e,#1f2230)}
.work-copy{left:124px;top:1820px;width:330px}
.work-copy p{margin-top:18px}

/* news */
.col-title{font-size:16px;color:var(--ink);font-weight:400}
.news{left:124px;top:2150px;width:250px}
.news-item{border-bottom:1px solid var(--line);padding:14px 0;font-size:8px;color:var(--ink);display:flex;justify-content:space-between}
.awards{left:440px;top:2150px;width:160px}
.awards p{font-size:7.5px;margin-top:10px}
.badge{width:80px;height:30px;background:var(--primary);margin-top:12px}
.trusted{left:660px;top:2150px;width:160px}
.trusted .row{display:grid;grid-template-columns:1fr 1fr;gap:12px;margin-top:14px}
.mark{height:18px;background:#d4d4dc;border-radius:2px}

/* footer */
.footer{left:0;top:2440px;width:880px;height:274px;background:var(--grey)}
.foot-brand{left:124px;top:2500px;display:flex;align-items:center;gap:7px;font-size:13px;font-weight:700;color:var(--primary)}
.foot-brand i{width:11px;height:11px;border-radius:50%;background:var(--primary);display:block}
.foot-contact{left:124px;top:2530px;font-size:7.5px;line-height:1.7}
.fcol{font-size:7.5px;line-height:1.8}
.fcol h4{font-size:9px;color:var(--ink);font-weight:600;margin-bottom:4px}
</style>
</head>
<body>
<main class="site">

  <section class="hero abs" role="img" aria-label="Photo of two colleagues reviewing a laptop in a server room"></section>

  <header>
    <div class="topbar abs">
      <span><svg width="9" height="9" viewBox="0 0 10 10"><path d="M2 1l2 2-1 1.5c.8 1.3 1.7 2.2 3 3L7.5 6l2 2-1.5 1.5C4.5 9 1 5.5.5 2z" fill="#9a9aa8"/></svg>+64 9 000 4821</span>
      <span>hello@larkwell.co.nz</span>
    </div>
    <div class="brand abs"><i></i>LARKWELL</div>
    <nav class="nav abs">
      <a>Home</a><a>Services</a><a>Products</a><a>About Us</a><a>Blogs</a><a>Contact Us</a>
    </nav>
  </header>

  <div class="hero-copy abs">
    <div class="eyebrow">Cyber security partners</div>
    <h1>Protect Your Business Against Cyber-Crime</h1>
    <div class="btns"><span class="btn solid">Our services</span><span class="btn line">Contact us</span></div>
  </div>

  <section>
    <h2 class="solutions-title abs">Larkwell<br><em>Solutions</em></h2>
    <p class="solutions-text abs">Larkwell is a New Zealand based security firm that helps mid to large enterprises understand, manage and reduce cyber risk. We work with finance, insurance and utility teams to protect their people, systems and data, turning complex threats into clear business decisions.</p>
  </section>

  <section>
    <div class="about-band abs"></div>
    <div class="about-img abs" role="img" aria-label="Photo of a team talking in a bright modern office"></div>
    <div class="about-copy abs">
      <h2>About <b>Larkwell</b></h2>
      <p>We are a team of analysts, engineers and advisors who believe security should enable growth. <b style="color:var(--ink)">Experienced, independent and practical</b>, we help leaders see their exposure and act on it with confidence.</p>
      <p>From risk reviews to managed tools, we stay beside our clients long after the first report is delivered.</p>
      <div class="more">Learn More <span>→</span></div>
    </div>
  </section>

  <section>
    <h2 class="services-title abs">Services <b>We Provide</b></h2>
    <div class="grid abs">
      <div class="shot" role="img" aria-label="Screenshot of the risk manager dashboard"></div>
      <div class="card"><h3>Current Risk Manager tool</h3><p>Track live exposure across systems and suppliers in one clear view.</p><div class="more">Read More →</div></div>
      <div class="shot" role="img" aria-label="Screenshot of a software rating table"></div>
      <div class="card"><h3>Software Rating</h3><p>Score the tools you rely on and spot weak links before attackers do.</p><div class="more">Read More →</div></div>
      <div class="card"><h3>Advanced Manager tool</h3><p>Deeper reporting and controls for larger teams with complex estates.</p><div class="more">Read More →</div></div>
      <div class="shot" role="img" aria-label="Screenshot of the advanced manager interface"></div>
      <div class="card"><h3>Stratus Shield</h3><p>Cloud delivered protection that blocks threats at the network edge.</p><div class="more">Read More →</div></div>
      <div class="shot" role="img" aria-label="Screenshot of the cloud protection console"></div>
    </div>
  </section>

  <section>
    <div class="work-band abs"></div>
    <div class="work-img abs" role="img" aria-label="Photo of engineers working in a data centre"></div>
    <div class="work-copy abs">
      <h2>What We Do, <b>How We Do It</b></h2>
      <p>We start by listening to how your business works, then map the risks that matter most. Our advisors combine proven frameworks with hands-on testing to build a plan that fits your budget, your people and your regulators.</p>
      <div class="more">Learn More →</div>
    </div>
  </section>

  <section>
    <div class="news abs">
      <h3 class="col-title">Recent News</h3>
      <div class="news-item"><span>Ransomware Protection</span><span>→</span></div>
      <div class="news-item"><span>Latest Threat Advisories</span><span>→</span></div>
    </div>
    <div class="awards abs">
      <h3 class="col-title">Awards</h3>
      <p>Security partner of the year 2022</p>
      <div class="badge" role="img" aria-label="Award badge"></div>
    </div>
    <div class="trusted abs">
      <h3 class="col-title">Trusted By</h3>
      <div class="row">
        <div class="mark" role="img" aria-label="Client logo"></div>
        <div class="mark" role="img" aria-label="Client logo"></div>
        <div class="mark" role="img" aria-label="Client logo"></div>
        <div class="mark" role="img" aria-label="Client logo"></div>
      </div>
    </div>
  </section>

  <footer>
    <div class="footer abs">
      <svg width="880" height="40" viewBox="0 0 880 40" style="position:absolute;left:0;top:0"><path d="M0 0h880v14C700 34 560 6 420 18S150 30 0 12z" fill="#ffffff"/></svg>
    </div>
    <div class="foot-brand abs"><i></i>LARKWELL</div>
    <div class="foot-contact abs">Level 4, 18 Harbour Lane<br>Auckland 1010<br>+64 9 000 4821<br>hello@larkwell.co.nz</div>
    <div class="fcol abs" style="left:470px;top:2500px"><h4>Company</h4>About Us<br>Careers<br>Blogs<br>Contact</div>
    <div class="fcol abs" style="left:580px;top:2500px"><h4>Partners</h4>Alliances<br>Resellers</div>
    <div class="fcol abs" style="left:690px;top:2500px"><h4>Alliance</h4>Technology Partners<br>Vendors<br>Integrations</div>
    <div class="fcol abs" style="left:470px;top:2590px"><h4>Services</h4>Risk Review<br>Managed Tools<br>Advisory</div>
    <div class="fcol abs" style="left:690px;top:2590px"><h4>Resources</h4>Site Map<br>Privacy Policy<br>GDPR</div>
  </footer>

</main>
</body>
</html>
```